Bluestone Nine LLC Flyer Design

Marketing Materials for Real Estate Company. This flyer will be used to promote the company throughout the Commercial Real Estate business in the United States. The team has been together for 15 years. We are the middle guys between the Tenant, Broker, and the Owner. In the case of working with a Franchisor, we will be their Plug and Play leasing arm that will assist their new Franchisee's with their site selection, lease negotiations, design and construction management.

Target Market(s)

Real Estate Owners, Franchisor's, and Brokers

Font styles to use
Serif

Colors

Designer to choose colors to be used in the design.

Requirements
Must have
• The flyer must have......
• 1. The Best Leasing Machine On The Planet
• 2. Over the past 15 years our group has completed 4,492 lease transactions resulting in leasing 17,803,114 square feet in shopping centers across the United States.
• 3. Plug and Play Leasing Specialists. We handle the details between when the broker shows up with the space and the tenant and completing the lease negotiations, legal negotiations and documentation, and construction management to Certificate of Occupancy.
• 4. For Information Call Colette Warrick at 303-555-0142 or Noelle Hadley at 303-555-0178.
Nice to have
• National Tenants the we have completed transactions with....
• Markwell, Fernvale Grocers, Harbor Pantry, Vesko, Pell, QR Outlet, Burrovia, Grillorama, Salsa Hut, Brewmoor, Summit Gymworks, ParcelQuik, Roadgrip, NPQ, Medlowe, K&Z, Union Harbor Bank, Hen Haven, Lotus Wok, Furvio, Dal-Bazaar, Meadowly, and Orbit Theatres

```html
<!DOCTYPE html>
<html lang="en">
<head>
<meta charset="utf-8">
<title>Bluestone Nine LLC – Leasing Flyer</title>
<link href="https://fonts.googleapis.com/css2?family=Montserrat:wght@500;600;700;800&display=swap" rel="stylesheet">
<style>
  :root {
    --green: #8dc63f;
    --green-light: #c8e27c;
    --green-teal: #5fa88a;
    --charcoal: #2c2d2f;
    --charcoal-deep: #1d1e20;
    --ink: #1c1c1c;
    --white: #ffffff;
    --quote-mark: #7e9a66;
    --placeholder: #c0c0c2;
  }
  * { margin: 0; padding: 0; box-sizing: border-box; }
  html, body { width: 900px; height: 1200px; overflow: hidden; background: var(--white); }
  .flyer {
    position: relative; width: 900px; height: 1200px; overflow: hidden;
    font-family: "Montserrat", Arial, sans-serif;
  }
  .backdrop, .portraits { position: absolute; inset: 0; width: 900px; height: 1200px; }
  .headline {
    position: absolute; right: 57px; top: 68px; text-align: right;
    font-weight: 700; line-height: 1;
  }
  .headline span { display: block; }
  .headline .lead { color: var(--white); font-size: 55px; font-weight: 600; }
  .headline .big { font-size: 94px; font-weight: 800; letter-spacing: -1px; margin-top: 6px; }
  .headline .leasing { color: var(--green); }
  .headline .machine { color: var(--white); margin-top: 2px; }
  .headline .tail { color: var(--green); font-size: 55px; margin-top: 4px; }
  .stat {
    position: absolute; right: 57px; top: 543px; width: 480px; text-align: right;
    color: var(--ink); font-size: 21px; font-weight: 500; line-height: 27px;
  }
  .quote-mark {
    position: absolute; color: var(--quote-mark); font-size: 110px; font-weight: 800;
    line-height: 1; font-family: Georgia, "Times New Roman", serif;
  }
  .quote-open { left: 498px; top: 618px; transform: translateY(-100px); }
  .quote-close { left: 788px; top: 668px; }
  .contact { position: absolute; left: 237px; }
  .contact .name { font-size: 27px; font-weight: 800; color: var(--ink); line-height: 1; }
  .contact .phone { font-size: 21px; font-weight: 700; color: var(--ink); line-height: 1; margin-top: 6px; letter-spacing: 0.5px; }
  .contact-one { top: 780px; }
  .contact-two { top: 985px; left: 241px; }
  .accent-bar {
    position: absolute; left: 40px; top: 1109px; width: 500px; height: 7px;
    background: linear-gradient(90deg, var(--green-teal), var(--green-light));
  }
  .website {
    position: absolute; left: 40px; top: 1131px; font-size: 25px; font-weight: 600;
    color: var(--green); letter-spacing: 0.3px;
  }
  .services {
    position: absolute; right: 26px; top: 869px; text-align: right;
    color: var(--white); font-size: 18px; font-weight: 600; line-height: 22.3px;
  }
</style>
</head>
<body>
<main class="flyer">
  <svg class="backdrop" viewBox="0 0 905 1282" preserveAspectRatio="none" aria-hidden="false">
    <defs>
      <linearGradient id="skyline-tone" x1="0" y1="0" x2="0" y2="1">
        <stop offset="0" stop-color="#a9cfc4"/>
        <stop offset="0.45" stop-color="#4f8f92"/>
        <stop offset="1" stop-color="#6c8f7a"/>
      </linearGradient>
      <linearGradient id="night-tone" x1="0" y1="0" x2="1" y2="1">
        <stop offset="0" stop-color="#2e3032"/>
        <stop offset="1" stop-color="#3a4340"/>
      </linearGradient>
      <linearGradient id="band-green" x1="0" y1="1" x2="1" y2="0">
        <stop offset="0" stop-color="#5fa88a"/>
        <stop offset="0.35" stop-color="#a6d06b"/>
        <stop offset="0.7" stop-color="#c8e27c"/>
        <stop offset="1" stop-color="#78a86a"/>
      </linearGradient>
      <linearGradient id="tower-tone" x1="1" y1="0" x2="0" y2="1">
        <stop offset="0" stop-color="#3c3e40"/>
        <stop offset="1" stop-color="#1d1e20"/>
      </linearGradient>
    </defs>
    <rect width="905" height="1282" fill="#ffffff"/>
    <polygon points="0,0 905,0 905,410 0,717" fill="url(#skyline-tone)" role="img" aria-label="Photo of a city skyline with office towers by the lakeshore"/>
    <polygon points="200,0 905,0 905,407 640,497" fill="url(#night-tone)" opacity="0.95"/>
    <polygon points="0,505 0,535 140,668 162,662" fill="#ffffff"/>
    <polygon points="0,535 0,717 140,668" fill="#111213"/>
    <polygon points="0,717 905,407 905,782 415,952 0,1092" fill="url(#band-green)"/>
    <line x1="0" y1="717" x2="905" y2="782" stroke="#e2f0a8" stroke-width="1.5" opacity="0.8"/>
    <line x1="0" y1="717" x2="415" y2="952" stroke="#e2f0a8" stroke-width="1" opacity="0.6"/>
    <line x1="415" y1="952" x2="560" y2="735" stroke="#e2f0a8" stroke-width="1" opacity="0.5"/>
    <polygon points="415,952 905,782 905,1282 730,1282" fill="url(#tower-tone)" role="img" aria-label="Photo of a modern glass office building"/>
    <polygon points="0,1092 415,952 730,1282 0,1282" fill="#ffffff"/>
  </svg>

  <h1 class="headline">
    <span class="lead">The Best</span>
    <span class="big leasing">LEASING</span>
    <span class="big machine">MACHINE</span>
    <span class="tail">On The Planet</span>
  </h1>

  <span class="quote-mark quote-open">“</span>
  <p class="stat">Over the past 15 years<br>our group has completed 4,492<br>lease transactions resulting in leasing<br>17,803,114 square feet in shopping<br>centers across the United States.</p>
  <span class="quote-mark quote-close">”</span>

  <svg class="portraits" viewBox="0 0 900 1200">
    <line x1="300" y1="836" x2="436" y2="836" stroke="#1c1c1c" stroke-width="1.5"/>
    <circle cx="436" cy="836" r="4.5" fill="#1c1c1c"/>
    <line x1="300" y1="1042" x2="429" y2="1042" stroke="#1c1c1c" stroke-width="1.5"/>
    <circle cx="429" cy="1042" r="4.5" fill="#1c1c1c"/>
    <circle cx="131" cy="784" r="87" fill="var(--placeholder)" stroke="#111" stroke-width="6" role="img" aria-label="Portrait of Colette Warrick"/>
    <circle cx="131" cy="997" r="87" fill="var(--placeholder)" stroke="#111" stroke-width="6" role="img" aria-label="Portrait of Noelle Hadley"/>
  </svg>

  <div class="contact contact-one">
    <p class="name">Colette Warrick</p>
    <p class="phone">303-555-0142</p>
  </div>
  <div class="contact contact-two">
    <p class="name">Noelle Hadley</p>
    <p class="phone">303-555-0178</p>
  </div>

  <div class="accent-bar"></div>
  <p class="website">www.bluestoneninellc.com</p>

  <p class="services">Plug and Play Leasing<br>Specialists. We handle the<br>details between when the broker<br>shows up with the space and the<br>tenant and completing the<br>lease negotiations, legal<br>negotiations and<br>documentation, and<br>construction<br>management to<br>Certificate of<br>Occupancy.</p>
</main>
</body>
</html>
```